Organic Herbs & Spices container

Greek startup company, which cultivate and trade spices and herbs (such as oregano, mint, thyme, sage etc.)

At present we are interested in only the type and shape of packaging which should be made by materials such as paper, cardboard, laminated paper and others based on paper or plastic.

Package size vary from 80g (2.82oz) - 300g (10.58oz). We are going to use the same packing for a variety of products with different information

* Please find attached our logo which should be included in the design.
* There is no company name available at the moment, however a name placeholder should be included.
* include a placeholder for the type of product (sage, oregano, mint, tea etc...).
* Each package should have a place in order to include product details and nutrition facts.

e.g.
xxxx (company name placeholder)
Sage (product type)
product details and nutrition facts.
Updates

Dear designers,first of all, thank you for your proposals. Please find bellow some updates for the project.- It is mandatory to include the logo into the design - Each package should be able to stored vertically - We are looking for one specific package design, please do not submit many variations of a certain package neither colour differentiations Thanks and good luck Added Wednesday, September 28, 2016

Please avoid the use of images. The same package will be used for all the kinds of products (only name and maybe colour will be different among different products. A transparent frame that will show the contents could be used too) Added Wednesday, September 28, 2016

Please find attached logo in EPS format

Our logo is the baseline, any concepts should be based on it. Try to avoid just adding the logo as a small sticker somewhere on the design. Please try to create around it at any way toy like. This could be, to visualize it as a 3D shape or object which can be used as the container of the products.

Reason: We would like to extend the time of the project. We believe that most of the submitted designs do not comply with our requirements.

Reason: We would like to see a bigger variety of ideas

Target Market(s)

Pretty much to anyone over 20 years old worldwide.

Industry/Entity Type

Nutrition

Requirements
Must have
• It should be attractive, easily recognized, simple yet innovative, durable, functional (easy to use) and easy to store.
Should not have
• Project must not include complex or obnoxious shapes and colours.

```html
<!DOCTYPE html>
<html lang="en">
<head>
<meta charset="utf-8">
<title>Organic Herbs Pyramid Pack – Dieline</title>
<link rel="stylesheet" href="https://fonts.googleapis.com/css2?family=Quicksand:wght@600&family=Lobster&family=Raleway:wght@500&family=Arimo&display=swap">
<style>
  :root {
    --leaf-dark: #2e4210;
    --leaf-mid: #4a6e2a;
    --leaf-bright: #6f8f2c;
    --gold: #f5b700;
    --gold-soft: #d9b23a;
    --ink: #2e4210;
    --paper: #ffffff;
  }
  html, body {
    margin: 0;
    padding: 0;
    width: 720px;
    height: 1200px;
    overflow: hidden;
    background: var(--paper);
  }
  .dieline { display: block; width: 720px; height: 1200px; }
  .panel { fill: var(--leaf-dark); stroke: var(--gold); stroke-width: 3; stroke-linejoin: round; }
  .pattern-panel { fill: url(#ornament-tone); stroke: var(--gold); stroke-width: 3; stroke-linejoin: round; }
  .pattern-side { fill: url(#ornament-side); stroke: var(--gold); stroke-width: 3; stroke-linejoin: round; }
  .info-box { fill: var(--leaf-mid); stroke: var(--gold); stroke-width: 3; }
  .brand-mark { fill: var(--leaf-bright); }
  .brand-name { font-family: "Quicksand", sans-serif; font-weight: 600; font-size: 24.5px; fill: var(--gold); letter-spacing: 0.3px; }
  .product-name { font-family: "Lobster", cursive; font-size: 48px; fill: var(--gold); }
  .herb-window { fill: url(#herb-tone); stroke: var(--gold); stroke-width: 2.5; }
  .template-label { font-family: "Raleway", sans-serif; font-weight: 500; font-size: 33px; fill: var(--ink); }
  .ingredients { font-family: "Arimo", Arial, sans-serif; font-size: 9.4px; fill: #ffffff; }
</style>
</head>
<body>
<svg class="dieline" viewBox="0 0 920 1500" preserveAspectRatio="xMidYMin meet" xmlns="http://www.w3.org/2000/svg">
  <defs>
    <linearGradient id="ornament-tone" x1="0" y1="0" x2="1" y2="1">
      <stop offset="0" stop-color="#e2bb45"/>
      <stop offset="0.25" stop-color="#9c8a2c"/>
      <stop offset="0.5" stop-color="#d9b23a"/>
      <stop offset="0.75" stop-color="#7f7a24"/>
      <stop offset="1" stop-color="#d9b23a"/>
    </linearGradient>
    <linearGradient id="ornament-side" x1="0" y1="0" x2="0" y2="1">
      <stop offset="0" stop-color="#6c6a1e"/>
      <stop offset="0.5" stop-color="#c9a435"/>
      <stop offset="1" stop-color="#6c6a1e"/>
    </linearGradient>
    <radialGradient id="herb-tone" cx="0.5" cy="0.5" r="0.6">
      <stop offset="0" stop-color="#a3a064"/>
      <stop offset="1" stop-color="#5f6a32"/>
    </radialGradient>
  </defs>

  <g class="face face-brand">
    <polygon class="panel" points="355,97 197,373 512,373"/>
    <circle class="brand-mark" cx="355" cy="262" r="50"/>
    <text class="brand-name" x="349" y="357" text-anchor="middle">COMPANY NAME</text>
  </g>

  <g class="face face-ornament-top" role="img" aria-label="Gold baroque scroll ornament on dark green">
    <polygon class="pattern-panel" points="355,97 670,97 512,373"/>
    <polygon class="pattern-side" points="670,97 692,135 535,373 512,373"/>
  </g>
  <g class="face face-ornament-left" role="img" aria-label="Gold baroque scroll ornament on dark green">
    <polygon class="pattern-panel" points="197,373 512,373 355,648"/>
  </g>

  <g class="face face-product">
    <polygon class="panel" points="512,373 670,648 355,648"/>
    <ellipse class="herb-window" cx="512" cy="515" rx="46" ry="68" role="img" aria-label="Clear window showing dried oregano leaves"/>
    <text class="product-name" x="510" y="630" text-anchor="middle">Oregano</text>
  </g>

  <g class="face face-info">
    <rect class="panel" x="355" y="648" width="315" height="312"/>
    <rect class="info-box" x="375" y="673" width="266" height="263"/>
    <text class="ingredients" x="382" y="698">
      <tspan x="382" dy="0">INGREDIENTS:</tspan>
      <tspan x="382" dy="11.6">Lorem ipsum dolor sit amet, consetetur sadipscing elitr,</tspan>
      <tspan x="382" dy="11.6">sed diam nonumy eirmod tempor invidunt ut labore et</tspan>
      <tspan x="382" dy="11.6">dolore magna aliquyam erat, sed diam voluptua. At vero</tspan>
      <tspan x="382" dy="11.6">eos et accusam et justo duo dolores et ea rebum. Stet</tspan>
      <tspan x="384" dy="11.6">clita kasd gubergren, no sea takimata sanctus est Lorem</tspan>
      <tspan x="382" dy="11.6">ipsum dolor sit amet. Lorem ipsum dolor sit amet,</tspan>
      <tspan x="382" dy="11.6">consetetur sadipscing elitr, sed diam nonumy eirmod</tspan>
      <tspan x="382" dy="11.6">tempor invidunt ut labore et dolore magna aliquyam erat,</tspan>
      <tspan x="382" dy="11.6">sed diam voluptua. At vero eos et accusam et justo duo</tspan>
      <tspan x="382" dy="11.6">dolores et ea rebum. Stet clita kasd gubergren, no sea</tspan>
      <tspan x="382" dy="11.6">takimata sanctus est Lorem ipsum dolor sit amet.</tspan>
      <tspan x="382" dy="11.6">Duis autem vel eum iriure dolor in hendrerit in vulputate</tspan>
      <tspan x="382" dy="11.6">velit esse molestie consequat, vel illum dolore eu feugiat</tspan>
      <tspan x="382" dy="11.6">nulla facilisis at vero eros et accumsan et iusto odio</tspan>
      <tspan x="382" dy="11.6">dignissim qui blandit praesent luptatum zzril delenit augue</tspan>
      <tspan x="382" dy="11.6">duis dolore te feugait nulla facilisi. Lorem ipsum dolor sit</tspan>
      <tspan x="382" dy="11.6">amet, consectetuer adipiscing elit, sed diam nonummy nibh</tspan>
      <tspan x="382" dy="11.6">euismod tincidunt ut laoreet dolore magna aliquam erat</tspan>
      <tspan x="384" dy="11.6">volutpat.</tspan>
    </text>
    <polygon class="panel" points="355,960 670,960 640,998 383,998"/>
  </g>

  <text class="template-label" x="725" y="375" text-anchor="middle">TEMPLATE</text>
</svg>
</body>
</html>
```